2 page Web Site Design (Coded), simple, not picky

I need a web portal for a PPC marketing business. I have the logo, some imagery, and some websites to base the design on.

***Background***
The name of the business is "Quiet Harbor Outreach Partners" or QHOP. We provide listings in a searchable database for Dental Sleep Medicine doctors. These are doctors who treat snoring/sleep apnea/and CPAP users with oral appliances. Client doctors will have their own "landing page website" where PPC prospects land from the PPC campaigns. Logos for supporting/landing page websites have been uploaded.
***End Background***

THIS website (for you to design) is to introduce doctors to the concept and detail the services. i.e. PPC campaign management services, listing on a national database of Dental Sleep Medicine practitioners, and a fully featured website dedicated to Snoring, Sleep Apnea, and CPAP Alternative treatment (those websites are "Farewell-Rumble.com", "Farewell-NightPause.com", and ""Farewell-MaskFree.com")

SEM websites whose look I enjoy are:

http://www.brivolta.com/marketing-services/pay-per-click/

http://www.quellandrift.com/welcome/pay-per-click-services/

http://www.tarnolux4co.com/marketing-services/paid-search-management/

The main colors are Red, White, & Blue. Red and blue used mostly for accents/emphasis.

The main/index page's purpose is to, as best possible, convey the idea of SEM campaign management with supporting websites being their best option for internet marketing!
The secondary page is just a slightly modified layout where details can be explained.

Target Market(s)

Dentists who practice Dental Sleep Medicine (see www.pqwrl.org)

Industry/Entity Type

Marketing

Requirements
Must have
• -Sign-up form for the generation of leads... Simple script that sends E-mail is fine... Doctor's Name, Business Name, Business Address, E-mail address, phone #.

-Graphics that will clearly describe the services being provided.

```html
<!DOCTYPE html>
<html lang="en">
<head>
<meta charset="utf-8">
<title>QHOP – Quiet Harbor Outreach Partners</title>
<link href="https://fonts.googleapis.com/css2?family=Arimo:wght@400;700&family=Open+Sans:wght@400;600&family=Questrial&display=swap" rel="stylesheet">
<style>
  :root {
    --brand-red: #b8242f;
    --button-red-dark: #a51f29;
    --brand-blue: #244a8c;
    --heading-blue: #2a4a92;
    --nav-blue: #5272ad;
    --nav-blue-dark: #3c5b98;
    --phone-ink: #14285a;
    --ink: #444444;
    --ink-soft: #555555;
    --panel-bg: #efefef;
    --panel-border: #b9b9b9;
    --field-border: #c8c8c8;
    --hero-light: #fbf3df;
    --hero-mid: #f1e2bd;
    --hero-dark: #6b4a36;
    --white: #ffffff;
  }
  * { box-sizing: border-box; margin: 0; padding: 0; }
  html, body { width: 1094px; height: 1200px; overflow: hidden; background: var(--white); }
  body { position: relative; font-family: "Arimo", Arial, sans-serif; color: var(--ink); }

  .site-header { position: absolute; left: 0; top: 0; width: 1094px; height: 134px; }
  .brand { position: absolute; left: 27px; top: 34px; display: flex; flex-direction: column; color: var(--brand-red); font-weight: 700; }
  .brand-row { display: flex; align-items: center; gap: 12px; }
  .brand-mark { width: 46px; height: 46px; border-radius: 50%; background: var(--brand-blue); }
  .brand-name { font-size: 44px; line-height: 46px; letter-spacing: 1px; }
  .brand-tagline { font-size: 13.5px; margin-top: 8px; }

  .call-line { position: absolute; right: 30px; top: 10px; font-family: "Open Sans", Arial, sans-serif; font-size: 17px; color: var(--brand-red); }
  .call-line strong { font-size: 21px; font-weight: 400; color: var(--phone-ink); margin-left: 4px; }

  .main-nav { position: absolute; top: 96px; left: 0; }
  .main-nav a { position: absolute; top: 0; height: 35px; line-height: 35px; text-align: center; font-size: 14.5px; color: #e9eef8; text-decoration: none;
    background: linear-gradient(var(--nav-blue), var(--nav-blue-dark)); border: 1px solid #33508a; border-bottom: none; border-radius: 3px 3px 0 0; }
  .main-nav a.is-current { background: linear-gradient(#d6343f, var(--button-red-dark)); border-color: #9a1c25; color: var(--white); }
  .header-rule { position: absolute; left: 0; top: 131px; width: 1094px; height: 3px; background: var(--brand-blue); }

  .hero { position: absolute; left: 0; top: 134px; width: 1094px; height: 408px; overflow: hidden;
    background: linear-gradient(90deg, var(--hero-mid) 0%, var(--hero-light) 35%, var(--hero-light) 70%, var(--hero-mid) 100%); }
  .hero-scene { position: absolute; left: 100px; top: 200px; width: 950px; height: 208px;
    background: linear-gradient(180deg, #8a6a54 0%, var(--hero-dark) 30%, #e9ecef 55%, #f7f8f9 100%); opacity: 0.55; }
  .hero-title { position: absolute; left: 111px; top: 46px; font-family: "Questrial", sans-serif; font-weight: 400; color: var(--heading-blue); font-size: 50px; line-height: 56px; }
  .hero-subtitle { position: absolute; left: 111px; top: 104px; font-family: "Questrial", sans-serif; color: #3d3d3d; font-size: 35px; line-height: 40px; }

  .signup-panel { position: absolute; left: 25px; top: 562px; width: 333px; height: 482px; background: var(--panel-bg); border: 1px solid var(--panel-border); }
  .signup-panel label { position: absolute; left: 33px; font-size: 13.5px; line-height: 16px; color: var(--ink-soft); }
  .signup-panel .field { position: absolute; left: 34px; width: 254px; height: 31px; background: var(--white); border: 1px solid var(--field-border); }
  .btn { position: absolute; display: block; color: var(--white); text-align: center; text-decoration: none; border: 1px solid #981c25; border-radius: 2px;
    background: linear-gradient(#d63540, var(--button-red-dark)); font-family: "Arimo", Arial, sans-serif; }
  .btn-submit { left: 177px; top: 424px; width: 110px; height: 33px; line-height: 31px; font-size: 16px; }
  .btn-small { height: 21px; line-height: 19px; font-size: 11px; }

  .section-heading { position: absolute; color: var(--heading-blue); font-weight: 400; }
  .welcome-heading { left: 391px; top: 570px; font-size: 26px; }
  .welcome-text { position: absolute; left: 391px; top: 613px; width: 676px; font-size: 13px; line-height: 18.8px; color: var(--ink); }
  .welcome-more { left: 391px; top: 739px; width: 72px; }

  .consultants-heading { left: 391px; top: 792px; font-size: 19.5px; }
  .consultant-photo { position: absolute; width: 131px; height: 96px; background: linear-gradient(135deg, #e8d2bf, #b8917a); }
  .consultant-photo.is-warm { background: linear-gradient(135deg, #f3e3c6, #c99a6a); }
  .consultant-photo.is-cool { background: linear-gradient(135deg, #dfe4e8, #a7b0b7); }

  .testimonials-heading { left: 734px; top: 792px; font-size: 19.5px; }
  .testimonial { position: absolute; left: 736px; width: 330px; font-size: 13px; line-height: 18.8px; color: var(--ink); }
  .testimonial cite { display: block; font-style: normal; color: var(--brand-red); margin-left: 3px; }
  .testimonials-more { left: 995px; top: 1024px; width: 71px; }

  .site-footer { position: absolute; left: 0; top: 1094px; width: 1094px; height: 106px; background: var(--brand-blue); color: var(--white);
    font-size: 12.5px; text-align: center; padding-top: 46px; }
  .site-footer a { color: var(--white); text-decoration: none; }
</style>
</head>
<body>
  <header class="site-header">
    <div class="brand">
      <div class="brand-row"><span class="brand-mark"></span><span class="brand-name">QHOP</span></div>
      <span class="brand-tagline">Quiet Harbor Outreach Partners</span>
    </div>
    <p class="call-line">Call: <strong>000 555 7373</strong></p>
    <nav class="main-nav">
      <a class="is-current" href="#" style="left:506px;width:94px">Home</a>
      <a href="#" style="left:603px;width:110px">About us</a>
      <a href="#" style="left:716px;width:110px">Services</a>
      <a href="#" style="left:829px;width:128px">Consultant</a>
      <a href="#" style="left:960px;width:108px">Contact us</a>
    </nav>
    <div class="header-rule"></div>
  </header>

  <section class="hero">
    <div class="hero-scene" role="img" aria-label="Photo of a couple in bed: one partner snores while the other covers their ears with a pillow"></div>
    <h1 class="hero-title">QHOP</h1>
    <p class="hero-subtitle">Quiet Harbor Outreach</p>
  </section>

  <form class="signup-panel">
    <label style="top:58px">Doctor's Name</label>
    <div class="field" style="top:85px"></div>
    <label style="top:131px">Business Name</label>
    <div class="field" style="top:155px"></div>
    <label style="top:204px">Business Address</label>
    <div class="field" style="top:227px"></div>
    <label style="top:277px">E-mail</label>
    <div class="field" style="top:300px"></div>
    <label style="top:350px">Phone</label>
    <div class="field" style="top:373px"></div>
    <a class="btn btn-submit" href="#">Submit</a>
  </form>

  <h2 class="section-heading welcome-heading">Welcome !</h2>
  <p class="welcome-text">Lorem Ipsum is simply dummy text of the printing and typesetting industry. Lorem Ipsum has been the industry's standard dummy text ever since the 1500s, when an unknown printer took a galley of type and scrambled it to make a type specimen book. It has survived not only five centuries, but also the leap into electronic typesetting, remaining essentially unchanged. It was popularised in the 1960s with the release of Varnett sheets containing Lorem Ipsum passages, and more recently with desktop publishing software like Oldane PageSetter including versions of Lorem Ipsum.</p>
  <a class="btn btn-small welcome-more" href="#">Read More</a>

  <h2 class="section-heading consultants-heading">Our Consultants</h2>
  <div class="consultant-photo" style="left:395px;top:835px" role="img" aria-label="Portrait of a consultant"></div>
  <div class="consultant-photo is-warm" style="left:549px;top:835px" role="img" aria-label="Consultant working at a desk"></div>
  <div class="consultant-photo is-cool" style="left:395px;top:948px" role="img" aria-label="Consultant in an office"></div>
  <div class="consultant-photo is-cool" style="left:549px;top:948px" role="img" aria-label="Smiling consultant wearing glasses"></div>

  <h2 class="section-heading testimonials-heading">Testmonials</h2>
  <blockquote class="testimonial" style="top:828px">Lorem Ipsum is simply dummy text of the printing and typesetting industry. Lorem Ipsum has been the industry's standard dummy text<cite>Mr. Tavel</cite></blockquote>
  <blockquote class="testimonial" style="top:938px">Lorem Ipsum is simply dummy text of the printing and typesetting industry. Lorem Ipsum has been the industry's standard dummy text<cite>Mr. Tavel</cite></blockquote>
  <a class="btn btn-small testimonials-more" href="#">Read More</a>

  <footer class="site-footer">
    © 2012 - <a href="#">Terms of Service</a> - <a href="#">Privacy Policy</a> - <a href="#">Program Policies</a>
  </footer>
</body>
</html>
```